Theater poster for a play about the Quillford siblings

We need a poster to promote our theatre show, Lanterns at Dusk: The Quillfords. We want an image that is edgy, modern, and hip. The show plays with the contrast between the modern age and the Victorian time period, so a possible design could reflect that. We are looking for an image that is more evocative and abstract, rather than something realistic like a photograph. The play deals with themes of alcoholism, incest, and incorporates the siblings' novels and poetry. We are also using kimonos from Japan so a possible design could also reference art or culture from there, but it must be in a very subtle way. The color red should be incorporated in a very strong way. The font should be very modern and hip.

```html
<!DOCTYPE html>
<html lang="en">
<head>
<meta charset="utf-8">
<title>Lanterns at Dusk: The Quillfords — Poster</title>
<link rel="stylesheet" href="https://fonts.googleapis.com/css2?family=Josefin+Slab:wght@400;600&family=Josefin+Sans:wght@400&family=Caveat:wght@500&display=swap">
<style>
  :root {
    --crimson: #5e0a1f;
    --crimson-light: #74142e;
    --plum: #4b1a56;
    --violet: #5a2a78;
    --ink-navy: #1e2560;
    --paper: #efe9ee;
    --paper-soft: #e2d6e2;
  }
  html, body {
    margin: 0;
    padding: 0;
    overflow: hidden;
    background: var(--crimson);
  }
  .poster {
    position: relative;
    width: 869px;
    height: 1200px;
    overflow: hidden;
    background: var(--crimson);
  }
  .poster__art {
    position: absolute;
    inset: 0;
    width: 869px;
    height: 1200px;
  }
  .title {
    position: absolute;
    left: 218px;
    top: 318px;
    margin: 0;
    color: var(--paper);
    font-family: "Josefin Slab", serif;
    font-weight: 600;
    line-height: 0.9;
  }
  .title__main {
    display: block;
    font-size: 96px;
    letter-spacing: 1px;
  }
  .title__small {
    font-size: 48px;
    color: var(--paper-soft);
    margin-left: 6px;
  }
  .title__second {
    display: block;
    font-size: 92px;
    color: var(--paper-soft);
    margin-top: 4px;
  }
  .title__sub {
    display: block;
    font-family: "Josefin Sans", sans-serif;
    font-weight: 400;
    font-size: 44px;
    margin-top: 18px;
    letter-spacing: 1px;
  }
  .dates {
    position: absolute;
    left: 278px;
    top: 632px;
    color: var(--paper);
    font-family: "Caveat", cursive;
    font-weight: 500;
    line-height: 0.95;
  }
  .dates__range { display: block; font-size: 50px; }
  .dates__time { display: block; font-size: 42px; margin-left: 78px; }
  .social {
    position: absolute;
    left: 16px;
    bottom: 16px;
    display: flex;
    align-items: center;
    gap: 10px;
  }
  .social__dot {
    width: 82px;
    height: 82px;
    border-radius: 50%;
    background: var(--ink-navy);
  }
  .social__name {
    color: var(--paper);
    font-family: "Josefin Sans", sans-serif;
    font-size: 18px;
    align-self: flex-start;
    margin-top: -6px;
  }
  .venue {
    position: absolute;
    left: 0;
    right: 0;
    bottom: 22px;
    text-align: center;
    color: var(--paper);
    font-family: "Josefin Sans", sans-serif;
    font-size: 25px;
    line-height: 1.05;
    letter-spacing: 0.5px;
  }
  .venue__name { display: block; margin-left: 40px; }
  .venue__address { display: block; margin-left: 120px; }
</style>
</head>
<body>
<main class="poster">
  <svg class="poster__art" viewBox="0 0 800 1105" preserveAspectRatio="none" aria-hidden="true">
    <rect width="800" height="1105" fill="var(--crimson)"/>
    <!-- pattern panels of the cross -->
    <rect x="110" y="0" width="512" height="1105" fill="var(--crimson-light)" opacity="0.55" role="img" aria-label="Faint kimono-inspired paisley pattern"/>
    <!-- large soft circles -->
    <circle cx="90" cy="440" r="200" fill="var(--crimson-light)" opacity="0.45"/>
    <circle cx="640" cy="420" r="190" fill="var(--crimson-light)" opacity="0.5"/>
    <circle cx="150" cy="1000" r="190" fill="#4a0616" opacity="0.55"/>
    <!-- horizontal bar of the cross -->
    <rect x="0" y="398" width="800" height="142" fill="var(--plum)" opacity="0.35"/>
    <!-- diagonal bands -->
    <polygon points="565,0 690,0 0,1000 0,805" fill="var(--violet)" opacity="0.85"/>
    <polygon points="705,0 800,0 800,110 380,700 330,700" fill="var(--violet)" opacity="0.8"/>
    <line x1="695" y1="0" x2="0" y2="1010" stroke="#7a1530" stroke-width="4"/>
    <!-- title panel -->
    <rect x="175" y="255" width="425" height="435" fill="var(--plum)" opacity="0.45"/>
    <circle cx="340" cy="400" r="170" fill="var(--crimson)" opacity="0.4"/>
    <rect x="387" y="590" width="214" height="103" fill="var(--violet)" opacity="0.75"/>
  </svg>

  <h1 class="title">
    <span class="title__main">LANTERNS<span class="title__small">at</span></span>
    <span class="title__second">DUSK</span>
    <span class="title__sub">THE QUILLFORDS</span>
  </h1>

  <p class="dates">
    <span class="dates__range">April 7 – April 12</span>
    <span class="dates__time">7:00pm – 1:00pm</span>
  </p>

  <div class="social">
    <span class="social__dot"></span>
    <span class="social__name">Linkway</span>
  </div>

  <p class="venue">
    <span class="venue__name">THEATRE LUMEN HALL</span>
    <span class="venue__address">42 HARROW LANE, TORONTO, ONTARIO M5T 0A0</span>
  </p>
</main>
</body>
</html>
```